Business Card Design Project for Food Export Company

Introduction about my Company Meng Tai Export Pte. Ltd.
(Meng Tai Food Export)
A Sole Distributor of various products:
Brand
Soy Powder (Brand: Bean Bean)
Coffee Powders (Brand: Ruvo)
OEM products
- Cocoa Powder
- Green Tea Powder
- Almond Powder
- Almond Flavour Powder
Showing we are professional with decades of experiences in terms of Product Quality and Trust.
NAMECARD - 2 sided namecard
Front:
Informations:
Darren Low
Sales Executive
+65 90428317
darrenlow@mtfoodtrade.example
Meng Tai Export Pte. Ltd.
42 Tuas Crescent, #03-08 Meridian Tower
Singapore 638102
Back:
Sole Distributor:
Bean Bean and Ruvoe
OEM Products:
Cocoa Powder / Green Tea Powder / Almond Powder / Almond Flavour Powder / Ice Cream Powder
I have attached Meng Tai Export's Logos. I've 2 currently, I would like to see some comparison.
Attached 2 Logos for Ruvo and Bean Bean.
Updates
Hi all designers,
I've revised the brief.
Have a look.
Thank you
Darren
Industry/Entity Type
Business
Look and feel

```html
<!DOCTYPE html>
<html lang="en">
<head>
<meta charset="utf-8">
<title>Meng Tai Food Export – Business Card</title>
<link href="https://fonts.googleapis.com/css2?family=Cinzel:wght@400;600;700&family=Montserrat:wght@600;700&display=swap" rel="stylesheet">
<style>
  :root {
    --canvas: #e9e9e7;
    --card: #050505;
    --card-sheen: #1a1a1a;
    --gold: #d9a84a;
    --gold-light: #f6dc7a;
    --gold-deep: #a9701f;
    --copper: #e0a060;
    --rule: #6b6b6b;
  }
  * { margin: 0; padding: 0; box-sizing: border-box; }
  html, body { width: 1200px; height: 1000px; overflow: hidden; }
  body { background: var(--canvas); position: relative; font-family: "Cinzel", serif; }

  .card {
    position: absolute;
    width: 755px; height: 397px;
    background: linear-gradient(115deg, var(--card) 0%, var(--card) 55%, var(--card-sheen) 68%, var(--card) 80%);
    border: 2px solid var(--gold);
    box-shadow: 0 6px 18px rgba(0,0,0,.35);
    overflow: hidden;
  }
  .card--front { left: 222px; top: 50px; }
  .card--back { left: 222px; top: 530px; }

  .corner { position: absolute; inset: 0; width: 100%; height: 100%; }

  .gold-text {
    background: linear-gradient(180deg, var(--gold-light) 0%, var(--gold) 50%, var(--gold-deep) 100%);
    -webkit-background-clip: text; background-clip: text;
    color: transparent;
  }

  /* Company mark block */
  .brand { position: absolute; left: 60px; top: 112px; width: 212px; text-align: center; color: var(--gold); }
  .brand__name { font-size: 42px; font-weight: 400; line-height: 70px; color: var(--gold); }
  .brand__rule { height: 1px; background: var(--rule); margin: 6px 0 4px; }
  .brand__division { font-size: 16px; letter-spacing: 2px; line-height: 22px; }
  .brand__company { font-size: 20px; letter-spacing: 3px; line-height: 26px; }
  .brand__tagline { font-size: 11px; letter-spacing: .5px; line-height: 14px; }

  /* Front */
  .contact { position: absolute; left: 350px; top: 92px; }
  .contact__name { font-family: "Montserrat", sans-serif; font-weight: 700; font-size: 24px; letter-spacing: 2px; color: var(--copper); }
  .contact__title { font-family: "Montserrat", sans-serif; font-weight: 600; font-size: 17px; letter-spacing: 1.5px; color: var(--gold-light); margin: 6px 0 0 8px; }
  .contact__list { list-style: none; margin-top: 40px; font-size: 13px; color: var(--copper); }
  .contact__list li { line-height: 24px; }
  .contact__list .phone { font-size: 15px; }
  .address { position: absolute; left: 0; right: 0; top: 296px; text-align: center; font-size: 15px; letter-spacing: 1px; color: var(--copper); padding-left: 20px; }
  .address p { line-height: 39px; }

  /* Back */
  .offer { position: absolute; left: 360px; top: 94px; color: var(--copper); }
  .offer__heading { font-size: 21px; font-weight: 600; line-height: 40px; }
  .offer__sub { font-size: 16px; font-weight: 600; margin-top: 2px; line-height: 34px; }
  .offer__list { list-style: none; font-size: 13px; margin: 6px 0 0 22px; }
  .offer__list li { line-height: 15px; }
</style>
</head>
<body>

<section class="card card--front" aria-label="Business card front">
  <svg class="corner" viewBox="0 0 755 397" preserveAspectRatio="none" aria-hidden="true">
    <defs>
      <linearGradient id="goldFront" x1="0" y1="0" x2="1" y2="1">
        <stop offset="0" stop-color="#f6dc7a"/>
        <stop offset=".5" stop-color="#d9a84a"/>
        <stop offset="1" stop-color="#a9701f"/>
      </linearGradient>
    </defs>
    <polygon points="597,0 755,0 755,140" fill="url(#goldFront)"/>
  </svg>

  <div class="brand">
    <div class="brand__name">Meng Tai</div>
    <div class="brand__rule"></div>
    <div class="brand__division gold-text">Food Export</div>
    <div class="brand__company gold-text">Meng Tai</div>
    <div class="brand__tagline gold-text">Sole Distributor of<br>Various Products</div>
    <div class="brand__rule"></div>
  </div>

  <div class="contact">
    <h1 class="contact__name">DARREN LOW</h1>
    <p class="contact__title">SALES EXECUTIVE</p>
    <ul class="contact__list">
      <li>E : darrenlow@mtfoodtrade.example</li>
      <li>W: www.mtfoodtrade.example</li>
      <li class="phone">C: +65 90428317</li>
    </ul>
  </div>

  <div class="address">
    <p>42 Tuas Crescent, #03-08 Meridian Tower</p>
    <p>Singapore 638102</p>
  </div>
</section>

<section class="card card--back" aria-label="Business card back">
  <svg class="corner" viewBox="0 0 755 397" preserveAspectRatio="none" aria-hidden="true">
    <defs>
      <linearGradient id="goldBack" x1="0" y1="0" x2="1" y2="1">
        <stop offset="0" stop-color="#f6dc7a"/>
        <stop offset=".5" stop-color="#d9a84a"/>
        <stop offset="1" stop-color="#a9701f"/>
      </linearGradient>
    </defs>
    <polygon points="0,250 0,397 175,397" fill="url(#goldBack)"/>
  </svg>

  <div class="brand">
    <div class="brand__name">Meng Tai</div>
    <div class="brand__rule"></div>
    <div class="brand__division gold-text">Food Export</div>
    <div class="brand__company gold-text">Meng Tai</div>
    <div class="brand__tagline gold-text">Sole Distributor of<br>Various Products</div>
    <div class="brand__rule"></div>
  </div>

  <div class="offer">
    <h2 class="offer__heading">Sole Distributor</h2>
    <p class="offer__sub">Bean Bean and Ruvoe</p>
    <p class="offer__sub">OEM Products:</p>
    <ul class="offer__list">
      <li>Cocoa Powder</li>
      <li>Green Tea Powder</li>
      <li>Almond Powder</li>
      <li>Almond Flavour Powder</li>
      <li>Ice Cream Powder</li>
    </ul>
  </div>
</section>

</body>
</html>
```